USB Business Card Design
Pelham Trowbridge Partners Chartered Accountants
Simple
Marcus Trowbridge, CA
Partner
20418-127 Ave
Edmonton, AB
T6K 4M3
T:855.316.2084
P:780.316.2084, D: 780.552.7391
F:780.317.6058
MTrowbridge@ptpca.com
www.ptpca.com
This is going to be printed onto a Business card sized USB stick. They are 2 sided, flashy and plastic coated. This is for extremely high end clients and need to look really amazing! We are open to all ideas, the bosses are partial to a simple look.

```html
<!DOCTYPE html>
<html lang="en">
<head>
<meta charset="utf-8">
<title>Pelham Trowbridge Partners – Business Card</title>
<link href="https://fonts.googleapis.com/css2?family=Open+Sans:wght@400;600;700&display=swap" rel="stylesheet">
<style>
  :root {
    --navy: #1b2f6e;
    --navy-deep: #14245a;
    --gold: #c08a3e;
    --gold-light: #e0b56c;
    --white: #ffffff;
    --stage: #e9e9ec;
  }
  * { margin: 0; padding: 0; box-sizing: border-box; }
  html, body {
    width: 1200px; height: 900px; overflow: hidden;
    background: var(--stage);
    font-family: "Open Sans", Arial, sans-serif;
  }
  .card {
    position: absolute; left: 75px; top: 150px;
    width: 1050px; height: 600px;
    background: var(--white);
    overflow: hidden;
    box-shadow: 0 10px 30px rgba(0,0,0,0.18);
  }
  .card-waves { position: absolute; inset: 0; width: 100%; height: 100%; }
  .brand { position: absolute; left: 70px; top: 70px; }
  .brand-name {
    display: flex; align-items: center; gap: 14px;
    color: var(--navy); font-weight: 700; font-size: 30px;
    letter-spacing: 0.5px; text-transform: uppercase;
  }
  .brand-mark { width: 26px; height: 26px; background: var(--navy); }
  .brand-tagline {
    margin-top: 8px; margin-left: 40px;
    color: var(--gold); font-weight: 600; font-size: 13px;
    letter-spacing: 5px; text-transform: uppercase;
  }
  .contact-list {
    position: absolute; left: 42px; top: 395px;
    list-style: none; color: var(--white); font-size: 14px; line-height: 1.2;
  }
  .contact-item { display: flex; align-items: flex-start; gap: 9px; margin-bottom: 4px; }
  .contact-icon { width: 16px; height: 16px; flex: none; margin-top: 1px; }
  .signatory { position: absolute; right: 70px; top: 415px; text-align: right; }
  .signatory-name { color: var(--gold-light); font-weight: 700; font-size: 24px; }
  .signatory-title { color: var(--white); font-size: 17px; margin-top: 6px; margin-right: 60px; }
</style>
</head>
<body>
<svg width="0" height="0" style="position:absolute">
  <defs>
    <symbol id="icon-pin" viewBox="0 0 16 16"><circle cx="8" cy="8" r="8" fill="#fff"/><path d="M8 3.5a3 3 0 0 0-3 3c0 2.2 3 6 3 6s3-3.8 3-6a3 3 0 0 0-3-3zm0 4.2a1.2 1.2 0 1 1 0-2.4 1.2 1.2 0 0 1 0 2.4z" fill="#1b2f6e"/></symbol>
    <symbol id="icon-phone" viewBox="0 0 16 16"><circle cx="8" cy="8" r="8" fill="#fff"/><path d="M5.2 4h1.6l.8 2-1 .8c.5 1.1 1.4 2 2.5 2.5l.8-1 2 .8v1.6c0 .5-.4.9-.9.9A7 7 0 0 1 4.3 4.9c0-.5.4-.9.9-.9z" fill="#1b2f6e"/></symbol>
    <symbol id="icon-fax" viewBox="0 0 16 16"><circle cx="8" cy="8" r="8" fill="#fff"/><rect x="4" y="6.5" width="8" height="4.5" rx="0.8" fill="#1b2f6e"/><rect x="5.5" y="4" width="5" height="2.5" fill="#1b2f6e"/><rect x="5.5" y="10" width="5" height="2" fill="#fff" stroke="#1b2f6e" stroke-width="0.8"/></symbol>
    <symbol id="icon-mail" viewBox="0 0 16 16"><circle cx="8" cy="8" r="8" fill="#fff"/><rect x="4" y="5" width="8" height="6" fill="#1b2f6e"/><path d="M4 5l4 3.3L12 5" fill="none" stroke="#fff" stroke-width="0.9"/></symbol>
    <symbol id="icon-web" viewBox="0 0 16 16"><circle cx="8" cy="8" r="8" fill="#fff"/><circle cx="8" cy="8" r="4" fill="none" stroke="#1b2f6e" stroke-width="1"/><ellipse cx="8" cy="8" rx="1.7" ry="4" fill="none" stroke="#1b2f6e" stroke-width="0.9"/><path d="M4 8h8" stroke="#1b2f6e" stroke-width="0.9"/></symbol>
  </defs>
</svg>

<main class="card">
  <svg class="card-waves" viewBox="0 0 1050 600" preserveAspectRatio="none" aria-hidden="true">
    <path d="M0 372 C 320 300, 620 430, 1050 262 L1050 600 L0 600 Z" fill="var(--navy)"/>
    <path d="M0 340 C 320 262, 620 400, 1050 222 L1050 250 C 620 420, 320 290, 0 362 Z" fill="var(--gold)"/>
    <path d="M0 318 C 330 250, 640 380, 1050 205 L1050 213 C 640 392, 330 262, 0 326 Z" fill="var(--gold-light)" opacity="0.8"/>
  </svg>

  <header class="brand">
    <div class="brand-name"><span class="brand-mark"></span>Pelham Trowbridge Partners</div>
    <div class="brand-tagline">Chartered Accountants</div>
  </header>

  <ul class="contact-list">
    <li class="contact-item"><svg class="contact-icon"><use href="#icon-pin"/></svg><span>20418-127 Ave<br>Edmonton, AB T6K 4M3</span></li>
    <li class="contact-item"><svg class="contact-icon"><use href="#icon-phone"/></svg><span>855.316.2084</span></li>
    <li class="contact-item"><svg class="contact-icon"><use href="#icon-phone"/></svg><span>780.316.2084</span></li>
    <li class="contact-item"><svg class="contact-icon"><use href="#icon-phone"/></svg><span>D: 780.552.7391</span></li>
    <li class="contact-item"><svg class="contact-icon"><use href="#icon-fax"/></svg><span>780.317.6058</span></li>
    <li class="contact-item"><svg class="contact-icon"><use href="#icon-mail"/></svg><span>MTrowbridge@ptpca.com</span></li>
    <li class="contact-item"><svg class="contact-icon"><use href="#icon-web"/></svg><span>www.ptpca.com</span></li>
  </ul>

  <section class="signatory">
    <div class="signatory-name">Marcus Trowbridge, CA</div>
    <div class="signatory-title">Partner</div>
  </section>
</main>
</body>
</html>
```